Flyer für Bikeshop
Zielgruppe
Bikeshop bikevermietung bikereparatur 365/365 offen
Aufgabenstellung
Der beigelegte Flyer sollte professionell gestaltet werden. Gerne sende ich diverse Fotos mit um sie evtl. zu verwenden. Ich habe keine präferenzen. Der Flyer sollte Jugendliche ansprechen. Der Flyer kann auch gänzlich ohne Fotos sein.

```html
<!DOCTYPE html>
<html lang="de">
<head>
<meta charset="utf-8">
<title>Velomont – Skills Training Flyer</title>
<link rel="stylesheet" href="https://fonts.googleapis.com/css2?family=Roboto+Slab:wght@700&family=Oswald:wght@500&display=swap">
<style>
  :root {
    --yellow: #ffec00;
    --black: #000000;
    --white: #ffffff;
    --page-bg: #ffffff;
    --photo-sky: #8fa6bf;
    --photo-trail: #7d7460;
    --photo-forest: #4d5a38;
    --photo-scree: #a9a392;
  }
  html, body {
    margin: 0;
    width: 1200px;
    height: 1200px;
    overflow: hidden;
    background: var(--page-bg);
  }
  .canvas { position: relative; width: 1200px; height: 1200px; }
  .flyer { position: absolute; top: 397px; width: 294px; height: 409px; display: block; }
  .flyer--front { left: 274px; }
  .flyer--back { left: 633px; }
  .headline { font-family: "Roboto Slab", Georgia, serif; font-weight: 700; fill: var(--white); }
  .brand-name { font-family: "Roboto Slab", Georgia, serif; font-weight: 700; fill: var(--black); letter-spacing: 5px; }
  .info { font-family: "Oswald", "Arial Narrow", sans-serif; font-weight: 500; font-size: 13px; }
  .info--dark { fill: var(--black); }
  .info--light { fill: var(--white); }
  .contact { font-family: "Roboto Slab", Georgia, serif; font-weight: 700; font-size: 13.5px; fill: var(--black); }
</style>
</head>
<body>
<main class="canvas">

  <!-- Front page -->
  <svg class="flyer flyer--front" viewBox="0 0 448 623" xmlns="http://www.w3.org/2000/svg">
    <defs>
      <linearGradient id="photoRidge" x1="0" y1="0" x2="0" y2="1">
        <stop offset="0" stop-color="var(--photo-sky)"/>
        <stop offset="1" stop-color="var(--photo-trail)"/>
      </linearGradient>
      <linearGradient id="photoTrail" x1="0" y1="0" x2="1" y2="1">
        <stop offset="0" stop-color="#8ea3b3"/>
        <stop offset="1" stop-color="#6f6a55"/>
      </linearGradient>
      <linearGradient id="photoForest" x1="0" y1="0" x2="1" y2="1">
        <stop offset="0" stop-color="#9fb5cf"/>
        <stop offset="0.5" stop-color="var(--photo-forest)"/>
        <stop offset="1" stop-color="#8a7a5e"/>
      </linearGradient>
    </defs>
    <rect class="flyer-bg" width="448" height="623" fill="var(--yellow)"/>

    <!-- white bands -->
    <polygon class="white-band" points="0,145 70,215 0,285" fill="var(--white)"/>
    <polygon class="white-band" points="0,480 95,480 0,575" fill="var(--white)"/>
    <polygon class="white-band" points="352,218 448,314 448,350 334,236" fill="var(--white)"/>
    <polygon class="white-band" points="92,488 334,246 346,258 104,500" fill="var(--white)"/>

    <!-- photo areas -->
    <polygon class="photo" role="img" aria-label="Foto: Mountainbiker auf einem Bergpfad über einem See"
      points="0,320 99,221 221,343 96,475 0,379" fill="url(#photoRidge)"/>
    <polygon class="photo" role="img" aria-label="Foto: Biker fährt einen steinigen Trail bergab"
      points="129,243 230,140 331,240 226,338" fill="url(#photoTrail)"/>
    <polygon class="photo" role="img" aria-label="Foto: Biker in einer Kurve zwischen Bäumen und Felsen"
      points="159,445 341,263 448,370 448,525 350,623 337,623" fill="url(#photoForest)"/>

    <!-- logo field -->
    <polygon class="logo-field" points="26,572 159,450 276,572 225,623 77,623" fill="var(--white)"/>
    <polyline points="16,572 159,440 286,572 235,623" fill="none" stroke="var(--black)" stroke-width="4"/>
    <line x1="16" y1="572" x2="67" y2="623" stroke="var(--black)" stroke-width="4"/>
    <line x1="352" y1="623" x2="448" y2="528" stroke="var(--black)" stroke-width="3"/>

    <circle cx="70" cy="558" r="7" fill="var(--black)"/>
    <text class="brand-name" x="84" y="564" font-size="17">VELOMONT</text>

    <!-- headline -->
    <rect x="36" y="50" width="374" height="67" fill="var(--black)"/>
    <text class="headline" x="223" y="101" font-size="50" text-anchor="middle">Free Bicycle</text>
    <rect x="18" y="135" width="410" height="66" fill="var(--black)"/>
    <text class="headline" x="223" y="186" font-size="50" text-anchor="middle">Skills Training</text>
  </svg>

  <!-- Back page -->
  <svg class="flyer flyer--back" viewBox="0 0 448 623" xmlns="http://www.w3.org/2000/svg">
    <defs>
      <linearGradient id="photoBackdrop" x1="0" y1="0" x2="1" y2="1">
        <stop offset="0" stop-color="#3f4a2e"/>
        <stop offset="0.5" stop-color="#6e6a5a"/>
        <stop offset="1" stop-color="var(--photo-scree)"/>
      </linearGradient>
      <linearGradient id="photoRider" x1="0" y1="0" x2="0" y2="1">
        <stop offset="0" stop-color="#b7c6d6"/>
        <stop offset="0.35" stop-color="var(--photo-forest)"/>
        <stop offset="1" stop-color="var(--photo-scree)"/>
      </linearGradient>
    </defs>
    <rect width="448" height="623" fill="url(#photoBackdrop)" role="img" aria-label="Hintergrundfoto: Bikereifen auf Felsboden mit Kiefern"/>

    <polygon class="info-panel" points="190,145 330,18 448,135 448,505 330,623 285,623 155,490" fill="var(--black)"/>
    <polygon class="info-panel--accent" points="0,165 110,55 275,220 65,428 0,362" fill="var(--yellow)"/>
    <polygon points="155,45 195,82 155,120 117,82" fill="var(--white)"/>
    <polygon points="380,15 422,57 380,100 338,57" fill="var(--yellow)"/>
    <polygon points="28,310 80,362 62,380 10,328" fill="var(--black)"/>
    <line x1="0" y1="510" x2="60" y2="450" stroke="var(--yellow)" stroke-width="3"/>
    <line x1="410" y1="570" x2="448" y2="530" stroke="var(--yellow)" stroke-width="3"/>
    <line x1="330" y1="623" x2="360" y2="592" stroke="var(--yellow)" stroke-width="3"/>

    <polygon role="img" aria-label="Foto: Biker mit rotem Rad auf steinigem Waldboden"
      points="148,315 282,440 148,560 24,438" fill="url(#photoRider)"
      stroke="var(--yellow)" stroke-width="5"/>

    <line x1="52" y1="147" x2="52" y2="288" stroke="var(--black)" stroke-width="2.5"/>
    <g class="info info--dark">
      <text x="72" y="155">GRATIS</text>
      <text x="72" y="172">FAHRTRAINING</text>
      <text x="72" y="206">FÜR ALLE JUGENDLICHEN</text>
      <text x="72" y="223">VON 8 - 14 JAHREN</text>
      <text x="72" y="257">JEDEN FREITAG</text>
      <text x="72" y="274">16:30 - 18:30</text>
    </g>

    <line x1="293" y1="136" x2="293" y2="280" stroke="var(--white)" stroke-width="2.5"/>
    <line x1="293" y1="355" x2="293" y2="500" stroke="var(--white)" stroke-width="2.5"/>
    <g class="info info--light">
      <text x="311" y="144">LEITUNG</text>
      <text x="311" y="178">LIO MARTEN</text>
      <text x="311" y="195">LEHRLING 1. JAHR</text>
      <text x="311" y="229">MIT EIGENEM</text>
      <text x="311" y="246">BIKE GRATIS</text>
      <text x="311" y="280">MIT MIETBIKE</text>
      <text x="311" y="297">FR. 20,-</text>
      <text x="311" y="361">BREMSTRAINING</text>
      <text x="311" y="395">FAHRKURSE</text>
      <text x="311" y="429">WHEELYTRAINING</text>
      <text x="311" y="463">TECHNIKTIPS</text>
      <text x="311" y="498">REPARATURKURSE</text>
    </g>

    <rect x="36" y="547" width="373" height="50" fill="var(--yellow)"/>
    <g class="contact">
      <text x="84" y="568" xml:space="preserve">via sur 14   |   7512 Val Vent</text>
      <text x="84" y="585" xml:space="preserve">info@velomont.ch   |   081 555 01 20</text>
    </g>
  </svg>

</main>
</body>
</html>
```